CD face & Jewel Case Design for Bayou Lanternmen Band

We need CD packaging (jewel case with 2 panel insert, and CD disc face) designed for the band Bayou Lanternmen.

Hear a sample of the music at: https://clipvault.example/watch/k7Rm2xQ9

It should say "Bayou Lanternmen" prominently on the cover and disc face since that's the album name too. The final design should communicate fun, energy and appeal to all ages.

There are many photos to choose from and we encourage you to be creative and follow your muse.

The text for album credits/liner notes is in the file "TEXT CREDITS".

We are open to your ideas. The templates have been uploaded as .psd files - if you need in another format, please specify thanks :)

Target Market(s)

fans of zydeco music, rock, counrty, all ages

Requirements
Nice to have
• maybe a retro look but not mandatory

```html
<!DOCTYPE html>
<html lang="en">
<head>
<meta charset="utf-8">
<title>Bayou Lanternmen — Album Cover</title>
<link href="https://fonts.googleapis.com/css2?family=Bodoni+Moda:opsz,wght@6..96,400&display=swap" rel="stylesheet">
<style>
  :root {
    --backdrop: #000000;
    --sky-top: #4c7c7a;
    --sky-mid: #8fb3ab;
    --sky-low: #c9e1d8;
    --ridge: #5d7267;
    --forest: #1f2e26;
    --forest-deep: #0c130f;
    --title: #ffffff;
    --mark: #0b0b0b;
  }
  html, body {
    margin: 0;
    padding: 0;
    width: 1200px;
    height: 1200px;
    overflow: hidden;
    background: var(--backdrop);
  }
  .canvas {
    position: relative;
    width: 1200px;
    height: 1200px;
    background: var(--backdrop);
  }
  .cover {
    position: absolute;
    left: 144px;
    top: 141px;
    width: 917px;
    height: 918px;
    overflow: hidden;
  }
  .cover-scene {
    position: absolute;
    inset: 0;
    background:
      linear-gradient(180deg,
        var(--sky-top) 0%,
        var(--sky-mid) 38%,
        var(--sky-low) 58%,
        var(--ridge) 70%,
        var(--forest) 86%,
        var(--forest-deep) 100%);
  }
  .band-mark {
    position: absolute;
    left: 0;
    right: 0;
    top: 102px;
    display: flex;
    justify-content: center;
    align-items: center;
    gap: 10px;
    font-family: "Bodoni Moda", "Didot", serif;
    font-weight: 400;
    font-size: 22px;
    letter-spacing: 2px;
    color: var(--mark);
  }
  .band-mark-dot {
    width: 18px;
    height: 18px;
    border-radius: 50%;
    background: var(--mark);
  }
  .title {
    position: absolute;
    left: 0;
    right: 0;
    margin: 0;
    text-align: center;
    font-family: "Bodoni Moda", "Didot", serif;
    font-weight: 400;
    color: var(--title);
    line-height: 1;
  }
  .band-name {
    top: 176px;
    font-size: 76px;
  }
  .band-name span {
    display: block;
    height: 74px;
  }
  .album-title {
    top: 494px;
    font-size: 45px;
  }
</style>
</head>
<body>
  <main class="canvas">
    <section class="cover">
      <div class="cover-scene" role="img" aria-label="Photograph of a snow-dusted rocky mountain peak with forested slopes under a pale teal sky"></div>
      <div class="band-mark">
        <span class="band-mark-dot"></span>
        <span class="band-mark-name">BAYOU LANTERNMEN</span>
      </div>
      <h1 class="title band-name"><span>BAYOU</span><span>LANTERNMEN</span></h1>
      <h2 class="title album-title">ALBUM TITLE</h2>
    </section>
  </main>
</body>
</html>
```